Modern business card design for professional copywriter

I'd like a business card design that I can use to have my cards printed out by plink.com as a squared corners business card (see artwork and design guidelines here: https://help.plink.com/hc/en-gb/sections/300481726-PLINK-Product-Templates)

The design should be clean and modern and reflect the colours, tone and branding on my website: https://noravestrel.com.au

Target Market(s)

Professionals, B2B small business owners

Industry/Entity Type

Business

Contact Information for Business Card

Nora Vestrel
m: 0427 593 864
e: nora@noravestrel.com.au
w: noravestrel.com.au

Font styles to use
Sans Serif

Requirements
Must have
• Tagline: "Smart copywriting for clever business people"
• Brand colours: fd8000, 009984, 666666 and black
Nice to have

```html
<!DOCTYPE html>
<html lang="en">
<head>
<meta charset="utf-8">
<title>Nora Vestrel – Business Card</title>
<link rel="stylesheet" href="https://fonts.googleapis.com/css2?family=Arimo&family=Open+Sans:wght@400;600&family=Questrial&display=swap">
<style>
  :root {
    --backdrop: #505050;
    --card: #ffffff;
    --teal: #009984;
    --orange: #fd8000;
    --grey: #666666;
    --ink: #000000;
  }
  html, body {
    margin: 0;
    padding: 0;
    width: 1200px;
    height: 1200px;
    overflow: hidden;
    background: var(--backdrop);
  }
  .stage {
    position: relative;
    width: 1200px;
    height: 1200px;
  }
  .card {
    position: absolute;
    width: 673px;
    height: 441px;
    background: var(--card);
  }
  .card--front { left: 263px; top: 126px; }
  .card--back  { left: 255px; top: 631px; }

  /* Front */
  .brand {
    position: absolute;
    left: 0;
    right: 0;
    top: 178px;
    display: flex;
    justify-content: center;
    align-items: center;
    gap: 14px;
  }
  .brand__dot {
    width: 22px;
    height: 22px;
    border-radius: 50%;
    background: var(--orange);
  }
  .brand__name {
    font-family: "Open Sans", sans-serif;
    font-weight: 600;
    font-size: 50px;
    line-height: 1;
    color: var(--teal);
    letter-spacing: -0.5px;
  }
  .tagline {
    position: absolute;
    left: 0;
    right: 0;
    top: 320px;
    text-align: center;
    font-family: "Arimo", sans-serif;
    font-size: 23px;
    color: var(--ink);
  }

  /* Back */
  .portrait {
    position: absolute;
    left: 100px;
    top: 138px;
    width: 184px;
    height: 184px;
    border-radius: 50%;
    box-sizing: border-box;
    border: 4px solid var(--teal);
    background: radial-gradient(circle at 50% 40%, #e8ddd0 0%, #d9d9d9 45%, #9aa3a0 100%);
  }
  .divider {
    position: absolute;
    left: 311px;
    top: 112px;
    width: 3px;
    height: 228px;
    background: var(--teal);
  }
  .contact {
    position: absolute;
    left: 340px;
    top: 134px;
  }
  .contact__name {
    font-family: "Open Sans", sans-serif;
    font-size: 25px;
    color: var(--grey);
    margin: 0 0 16px 0;
    line-height: 1.2;
  }
  .contact__list {
    list-style: none;
    margin: 0;
    padding: 0;
  }
  .contact__item {
    display: flex;
    align-items: center;
    height: 37px;
    margin-bottom: 10px;
    font-family: "Questrial", sans-serif;
    font-size: 15.5px;
    color: var(--grey);
    letter-spacing: 0.4px;
  }
  .contact__icon {
    width: 37px;
    height: 37px;
    margin-right: 16px;
    flex: none;
  }
  .contact__icon--teal { background: var(--teal); }
  .contact__icon--orange { background: var(--orange); }
  .contact__icon svg { display: block; }
</style>
</head>
<body>
<main class="stage">

  <section class="card card--front">
    <div class="brand">
      <span class="brand__dot"></span>
      <span class="brand__name">Nora Vestrel</span>
    </div>
    <p class="tagline">Smart copywriting for clever business people</p>
  </section>

  <section class="card card--back">
    <div class="portrait" role="img" aria-label="Portrait photo of Nora Vestrel"></div>
    <div class="divider"></div>
    <div class="contact">
      <h1 class="contact__name">Nora Vestrel</h1>
      <ul class="contact__list">
        <li class="contact__item">
          <span class="contact__icon contact__icon--teal">
            <svg width="37" height="37" viewBox="0 0 37 37" aria-hidden="true">
              <path d="M12 9c1-1 2-1 3 0l2 3c.6 1 .4 2-.4 2.6l-1.2 1c1 2.3 2.8 4.1 5 5.2l1-1.2c.7-.8 1.7-1 2.6-.4l3 2c1 .7 1 2 0 3l-1.3 1.3c-1.5 1.5-4 1.4-6.5-.2-3.3-2-6-4.8-8-8-1.5-2.6-1.7-5-.2-6.5z" fill="#fff"/>
            </svg>
          </span>
          0427 593 864
        </li>
        <li class="contact__item">
          <span class="contact__icon contact__icon--orange">
            <svg width="37" height="37" viewBox="0 0 37 37" aria-hidden="true" fill="none" stroke="#fff" stroke-width="1.6">
              <circle cx="18.5" cy="18.5" r="9"/>
              <ellipse cx="18.5" cy="18.5" rx="4" ry="9"/>
              <line x1="9.5" y1="18.5" x2="27.5" y2="18.5"/>
              <line x1="11" y1="14" x2="26" y2="14"/>
              <line x1="11" y1="23" x2="26" y2="23"/>
            </svg>
          </span>
          noravestrel.com.au
        </li>
        <li class="contact__item">
          <span class="contact__icon contact__icon--teal">
            <svg width="37" height="37" viewBox="0 0 37 37" aria-hidden="true" fill="none" stroke="#fff" stroke-width="1.6">
              <rect x="9" y="12" width="19" height="13"/>
              <polyline points="9,12 18.5,20 28,12"/>
              <line x1="9" y1="25" x2="15.5" y2="18"/>
              <line x1="28" y1="25" x2="21.5" y2="18"/>
            </svg>
          </span>
          nora@noravestrel.com.au
        </li>
      </ul>
    </div>
  </section>

</main>
</body>
</html>
```